Fixed price car insurance banner ad for insurance broker

We need a banner ad for addition to web pages and which will advertise an innovative insurance product we are selling.

We are an insurance broker and our product is a fixed price car insurance product.

The banner ad needs to display the company logo. This will be uploaded within the file upload section.

The remainder of the banner ad needs to explain what we are offering and also include the gear stick picture for impact.

We would like to see colours that tie in with the corporate colours, or alternative are striking and have presence on even the busiest web page I.e. Black banner and silver / white text. Please see the file upload for a sample of the brochure we are preparing for this product.

Target Market(s)

Private and commercial clients with both regular and high value motor vehicles.

Industry/Entity Type

Car Insurance

Font styles to use
Serif
Sans Serif

Colors

Designer to choose colors to be used in the design.

Requirements
Must have
• The banner must have the company logo on both pages.

I would like the advert to scroll / roll / fade or other between two pages displaying the following text:

Page 1
"Motor Insurance Scheme"
"Anything But Standard"
and including the gear knob picture

Page 2
Any Driver, Any Car, No Forms and One Flat Premium*

On clicking the banner ad, this will open an email, pre populated with email contact to request more detail.

Nice to have
• Open to your suggestions on this
Should not have
• Nothing at this stage. I will guide you when the ads are being submitted.

```html
<!DOCTYPE html>
<html lang="en">
<head>
<meta charset="utf-8">
<title>Halden Cover – Motor Insurance Banners</title>
<link rel="stylesheet" href="https://fonts.googleapis.com/css2?family=Electrolize&family=Open+Sans:wght@400&family=Marcellus+SC&display=swap">
<style>
  :root {
    --page: #ffffff;
    --label: #1a1a1a;
    --banner-black: #050505;
    --banner-dark: #121418;
    --panel-grey: #1e1f22;
    --silver: #c9ccd3;
    --white: #f4f4f4;
    --accent-red: #e01b1b;
    --car-red: #d8251c;
    --car-deep: #7a0d0a;
    --knob-light: #e9eaec;
    --knob-dark: #7d8087;
  }
  * { margin: 0; padding: 0; box-sizing: border-box; }
  html, body { width: 1200px; height: 900px; overflow: hidden; background: var(--page); }
  .canvas { position: relative; width: 1200px; height: 900px; }

  .size-label {
    position: absolute;
    font-family: "Electrolize", sans-serif;
    font-size: 24px;
    color: var(--label);
    letter-spacing: 0.5px;
  }
  .size-label--large { left: 30px; top: 50px; }
  .size-label--small { left: 302px; top: 562px; }

  .banner { position: absolute; overflow: hidden; background: var(--banner-black); }
  .banner--large { left: 21px; width: 1154px; height: 142px; }
  .banner--small { left: 301px; width: 594px; height: 73px; }
  .banner--offer-large { top: 105px; }
  .banner--scheme-large { top: 320px; }
  .banner--offer-small { top: 610px; }
  .banner--scheme-small { top: 742px; }

  .banner--offer { background: linear-gradient(90deg, #0b0b0b 0%, #151515 45%, #0a0a0a 100%); }
  .banner--scheme { background: radial-gradient(ellipse at 55% 80%, #3a0c0c 0%, #16161a 45%, #08080a 100%); }

  .brand-name {
    position: absolute;
    font-family: "Open Sans", sans-serif;
    font-weight: 400;
    color: var(--silver);
    text-transform: uppercase;
    line-height: 1.1;
  }
  .banner--large .brand-name { left: 24px; top: 22px; font-size: 34px; letter-spacing: 9px; }
  .banner--small .brand-name { left: 12px; top: 11px; font-size: 17px; letter-spacing: 4.5px; }

  .photo { position: absolute; }
  .photo--car { background: linear-gradient(120deg, #1a1010 0%, var(--car-deep) 18%, var(--car-red) 48%, #f0584c 62%, var(--car-red) 78%, #3a0806 100%); }
  .banner--large .photo--car { left: 680px; top: 0; width: 474px; height: 142px; }
  .banner--small .photo--car { left: 350px; top: 0; width: 244px; height: 73px; }

  .photo--knob {
    border-radius: 50%;
    background: radial-gradient(circle at 40% 35%, var(--knob-light) 0%, #b9bbc0 45%, var(--knob-dark) 80%, #2a2b2e 100%);
  }
  .banner--offer-large .photo--knob { left: 532px; top: 8px; width: 132px; height: 132px; }
  .banner--offer-small .photo--knob { left: 274px; top: 4px; width: 68px; height: 68px; }
  .banner--scheme-large .photo--knob { left: 1018px; top: 5px; width: 136px; height: 136px; }
  .banner--scheme-small .photo--knob { left: 523px; top: 3px; width: 70px; height: 70px; }

  .offer-line {
    position: absolute;
    font-family: "Electrolize", sans-serif;
    color: var(--white);
    white-space: nowrap;
    text-shadow: 0 0 3px #000;
  }
  .banner--large .offer-line { left: 308px; top: 50px; font-size: 34px; }
  .banner--small .offer-line { left: 158px; top: 26px; font-size: 17.5px; }

  .scheme-copy { position: absolute; text-align: center; }
  .banner--large .scheme-copy { left: 330px; top: 24px; width: 640px; }
  .banner--small .scheme-copy { left: 160px; top: 12px; width: 360px; }

  .scheme-title {
    font-family: "Open Sans", sans-serif;
    font-weight: 400;
    color: var(--white);
    line-height: 1.1;
  }
  .banner--large .scheme-title { font-size: 49px; }
  .banner--small .scheme-title { font-size: 26px; }

  .scheme-tagline {
    font-family: "Marcellus SC", serif;
    color: var(--accent-red);
    letter-spacing: 1px;
    line-height: 1.2;
  }
  .banner--large .scheme-tagline { font-size: 25px; margin-top: 4px; }
  .banner--small .scheme-tagline { font-size: 13px; margin-top: 1px; }
</style>
</head>
<body>
<main class="canvas">
  <p class="size-label size-label--large">728 x90</p>

  <section class="banner banner--large banner--offer banner--offer-large">
    <div class="brand-name">Halden<br>Cover</div>
    <div class="photo photo--car" role="img" aria-label="Red sports car with raised doors"></div>
    <div class="photo photo--knob" role="img" aria-label="Chrome gear knob with shift pattern"></div>
    <p class="offer-line">Any Driver, Any Car, No Forms &nbsp;&amp;&nbsp; One Flat Premium</p>
  </section>

  <section class="banner banner--large banner--scheme banner--scheme-large">
    <div class="brand-name">Halden<br>Cover</div>
    <div class="scheme-copy">
      <h2 class="scheme-title">Motor Insurance Scheme</h2>
      <p class="scheme-tagline">Anything But Standard</p>
    </div>
    <div class="photo photo--knob" role="img" aria-label="Chrome gear knob with shift pattern"></div>
  </section>

  <p class="size-label size-label--small">468 x60</p>

  <section class="banner banner--small banner--offer banner--offer-small">
    <div class="brand-name">Halden<br>Cover</div>
    <div class="photo photo--car" role="img" aria-label="Red sports car with raised doors"></div>
    <div class="photo photo--knob" role="img" aria-label="Chrome gear knob with shift pattern"></div>
    <p class="offer-line">Any Driver, Any Car, No Forms &nbsp;&amp;&nbsp; One Flat Premium</p>
  </section>

  <section class="banner banner--small banner--scheme banner--scheme-small">
    <div class="brand-name">Halden<br>Cover</div>
    <div class="scheme-copy">
      <h2 class="scheme-title">Motor Insurance Scheme</h2>
      <p class="scheme-tagline">Anything But Standard</p>
    </div>
    <div class="photo photo--knob" role="img" aria-label="Chrome gear knob with shift pattern"></div>
  </section>
</main>
</body>
</html>
```